BEACON CABS

Taxi card design

Need changes very slow in replying to my messages.

Target Market(s)

Customers

Industry/Entity Type

Taxi

Contact Information for Business Card

See previous design

Font styles to use
Sans Serif

Colors
A7469A
B969AE
D3A5CF
EDDBEB
F8F0F9
6B429C
8869AF
B7A5CE
E3DAEB
F3F0F8

Requirements
Nice to have
• We are in the business of looking after people, not just driving vehicles front
Should not have
• Front number 01632 480 480 needs to big big

```html
<!DOCTYPE html>
<html lang="en">
<head>
<meta charset="utf-8">
<title>Beacon Cabs – Business Card</title>
<link rel="stylesheet" href="https://fonts.googleapis.com/css2?family=Poppins:wght@400;600;700&family=Oswald:wght@500;600&family=Michroma&display=swap">
<style>
:root{
  --plum:#A7469A;
  --orchid:#B969AE;
  --lilac:#D3A5CF;
  --blush:#EDDBEB;
  --mist:#F8F0F9;
  --violet:#6B429C;
  --lavender:#8869AF;
  --haze:#B7A5CE;
  --ink:#0d0d0f;
  --paper:#ffffff;
  --stage:#ffffff;
}
*{margin:0;padding:0;box-sizing:border-box}
html,body{width:1200px;height:2239px;overflow:hidden;background:var(--stage)}
.canvas{position:relative;width:1200px;height:2239px}
.card{position:absolute;left:80px;width:1040px;height:594px;box-shadow:0 6px 14px rgba(0,0,0,.25);overflow:hidden}
.card--front{top:455px;background:linear-gradient(180deg,var(--plum) 0%,#8a3a96 50%,var(--violet) 100%)}
.card--back{top:1189px;background:var(--paper)}

/* front */
.front-name{position:absolute;left:0;right:0;top:150px;text-align:center;font:700 112px/1 'Poppins',sans-serif;color:var(--paper);letter-spacing:-1px}
.front-phone{position:absolute;left:160px;top:350px;width:720px;height:94px;background:var(--ink);border-radius:14px 28px 14px 14px;display:flex;align-items:center;justify-content:center;gap:22px}
.front-phone__number{font:400 50px/1 'Michroma',sans-serif;color:var(--paper)}
.front-band{position:absolute;left:0;right:0;top:530px;height:34px;background:linear-gradient(90deg,var(--blush),var(--lilac),var(--blush))}

/* back */
.back-strip{position:absolute;left:0;top:0;width:34px;height:100%;background:linear-gradient(180deg,var(--plum),var(--violet),var(--plum))}
.back-name{position:absolute;left:68px;top:58px;font:700 62px/1 'Poppins',sans-serif;color:var(--ink);letter-spacing:-1px;display:flex;align-items:center;gap:14px}
.back-name__mark{width:22px;height:22px;border-radius:50%;background:var(--plum)}
.services{position:absolute;left:66px;top:186px;list-style:none}
.service{display:flex;align-items:center;height:55px;font:600 31px/1 'Poppins',sans-serif;color:var(--ink)}
.service__icon{width:42px;height:42px;border-radius:8px;background:linear-gradient(180deg,var(--plum),var(--violet));margin-right:34px}
.contacts{position:absolute;left:628px;top:90px;list-style:none;font:400 22px/1.35 'Poppins',sans-serif;color:var(--ink)}
.contact{display:flex;align-items:flex-start;gap:12px;margin-bottom:4px}
.contact svg{flex:0 0 24px;margin-top:3px}
.service-hours{position:absolute;left:628px;top:314px;font:600 66px/1 'Oswald',sans-serif;color:var(--ink);letter-spacing:-1px}
.service-hours__accent{color:var(--violet)}
.lines{position:absolute;left:64px;top:386px;display:flex;gap:13px}
.line{width:298px;height:49px;border-radius:10px 22px 6px 6px;background:linear-gradient(180deg,var(--plum),var(--violet));display:flex;align-items:center;padding-left:14px;gap:14px;font:500 31px/1 'Oswald',sans-serif;color:var(--paper)}
.main-phone{position:absolute;left:124px;top:464px;display:flex;align-items:center;gap:14px}
.main-phone__icon{width:50px;height:50px;border-radius:10px;background:linear-gradient(180deg,var(--plum),var(--violet));display:flex;align-items:center;justify-content:center}
.main-phone__number{font:400 58px/1 'Michroma',sans-serif;color:var(--ink)}
</style>
</head>
<body>
<main class="canvas">

  <section class="card card--front" aria-label="Card front">
    <h1 class="front-name">Beacon Cabs</h1>
    <div class="front-phone">
      <svg width="46" height="46" viewBox="0 0 24 24" aria-hidden="true"><rect x="1" y="1" width="22" height="22" rx="6" fill="#fff"/><path d="M8 6c1 0 1.6 2 2 3 .3.7-1 1.4-.8 2 .6 1.5 1.8 2.8 3.4 3.5.6.2 1.3-1.1 2-.8 1 .4 3 1 3 2 0 1.4-1.5 2.3-2.6 2.1C10.5 17 7 13.5 6.2 9 6 7.7 6.8 6 8 6z" fill="#0d0d0f"/></svg>
      <span class="front-phone__number">01632 480 480</span>
    </div>
    <div class="front-band" role="img" aria-label="Chequered taxi band"></div>
  </section>

  <section class="card card--back" aria-label="Card back">
    <div class="back-strip" role="img" aria-label="Chequered taxi strip"></div>
    <h2 class="back-name"><span>Beacon Cabs</span><span class="back-name__mark"></span></h2>

    <ul class="services">
      <li class="service"><span class="service__icon"></span>AIRPORT TRANSFERS</li>
      <li class="service"><span class="service__icon"></span>MINIBUSES</li>
      <li class="service"><span class="service__icon"></span>SCHOOL TRANSPORT</li>
    </ul>

    <ul class="contacts">
      <li class="contact"><svg width="24" height="24" viewBox="0 0 24 24" aria-hidden="true"><path d="M7 3c1.2 0 2 2.6 2.4 3.8.3.9-1.3 1.7-1 2.5.8 2 2.4 3.6 4.4 4.4.8.3 1.6-1.3 2.5-1 1.2.4 3.8 1.2 3.8 2.4 0 1.8-2 3-3.4 2.7C9.9 16.8 6.2 13.1 4.2 7.3 3.9 5.4 5.2 3 7 3z" fill="#6B429C"/></svg>0800 555 0 188</li>
      <li class="contact"><svg width="24" height="24" viewBox="0 0 24 24" aria-hidden="true"><rect x="2" y="5" width="20" height="14" rx="1" fill="#6B429C"/><path d="M2 6l10 7 10-7" stroke="#fff" stroke-width="1.6" fill="none"/></svg>hello@beaconcabs.co.uk</li>
      <li class="contact"><svg width="24" height="24" viewBox="0 0 24 24" aria-hidden="true"><circle cx="12" cy="12" r="10" fill="#6B429C"/><path d="M2 12h20M12 2c3 3 3 17 0 20M12 2c-3 3-3 17 0 20" stroke="#fff" stroke-width="1.3" fill="none"/></svg>www.beaconcabs.co.uk</li>
      <li class="contact"><svg width="24" height="24" viewBox="0 0 24 24" aria-hidden="true"><path d="M12 2a7 7 0 0 0-7 7c0 5 7 13 7 13s7-8 7-13a7 7 0 0 0-7-7z" fill="#6B429C"/><circle cx="12" cy="9" r="2.6" fill="#fff"/></svg><span>Harbour Chapel Hall<br>Mill Lane Northbridge<br>NB4 7QX</span></li>
    </ul>

    <p class="service-hours"><span class="service-hours__accent">24/7</span> SERVICE</p>

    <div class="lines">
      <div class="line"><svg width="30" height="30" viewBox="0 0 24 24" aria-hidden="true"><rect x="1" y="1" width="22" height="22" rx="6" fill="#fff"/><path d="M8 6c1 0 1.6 2 2 3 .3.7-1 1.4-.8 2 .6 1.5 1.8 2.8 3.4 3.5.6.2 1.3-1.1 2-.8 1 .4 3 1 3 2 0 1.4-1.5 2.3-2.6 2.1C10.5 17 7 13.5 6.2 9 6 7.7 6.8 6 8 6z" fill="#8a3a96"/></svg>01632 61 61 61</div>
      <div class="line"><svg width="30" height="30" viewBox="0 0 24 24" aria-hidden="true"><rect x="1" y="1" width="22" height="22" rx="6" fill="#fff"/><path d="M8 6c1 0 1.6 2 2 3 .3.7-1 1.4-.8 2 .6 1.5 1.8 2.8 3.4 3.5.6.2 1.3-1.1 2-.8 1 .4 3 1 3 2 0 1.4-1.5 2.3-2.6 2.1C10.5 17 7 13.5 6.2 9 6 7.7 6.8 6 8 6z" fill="#8a3a96"/></svg>01632 24 24 24</div>
      <div class="line"><svg width="30" height="30" viewBox="0 0 24 24" aria-hidden="true"><rect x="1" y="1" width="22" height="22" rx="6" fill="#fff"/><path d="M8 6c1 0 1.6 2 2 3 .3.7-1 1.4-.8 2 .6 1.5 1.8 2.8 3.4 3.5.6.2 1.3-1.1 2-.8 1 .4 3 1 3 2 0 1.4-1.5 2.3-2.6 2.1C10.5 17 7 13.5 6.2 9 6 7.7 6.8 6 8 6z" fill="#8a3a96"/></svg>01632 73 55 11</div>
    </div>

    <div class="main-phone">
      <span class="main-phone__icon"><svg width="32" height="32" viewBox="0 0 24 24" aria-hidden="true"><path d="M7 3c1.2 0 2 2.6 2.4 3.8.3.9-1.3 1.7-1 2.5.8 2 2.4 3.6 4.4 4.4.8.3 1.6-1.3 2.5-1 1.2.4 3.8 1.2 3.8 2.4 0 1.8-2 3-3.4 2.7C9.9 16.8 6.2 13.1 4.2 7.3 3.9 5.4 5.2 3 7 3z" fill="#fff"/></svg></span>
      <span class="main-phone__number">01632 480 480</span>
    </div>
  </section>

</main>
</body>
</html>
```